2 Page Brochure - Commercial Roofing Company

We are looking for a double sided brochure, full color, for our commercial roofing company that tells customers a little bit about the company, what we do, and shows a few pictures.
The brochure would need to have our logo and color scheme that coordinates with that logo.
I have uploaded our logo, some ideas I had, and then the idea list also has our website on there if you'd like to take a look around there for some more ideas.
I have also uploaded some photos we'd like to use.
Page size should be 8.5" x 11".
Target Market(s)
Commercial Property Owners
Other font styles liked:
- Match logo font ideally so it's cohesive, but whatever looks best

```html
<!DOCTYPE html>
<html lang="en">
<head>
<meta charset="utf-8">
<title>R&amp;K Roofing – Commercial Roofing Brochure</title>
<link href="https://fonts.googleapis.com/css2?family=Montserrat:wght@400;500;600;700;800;900&display=swap" rel="stylesheet">
<style>
:root{
  --ink:#222222;
  --ink-soft:#2c2c2c;
  --orange:#e8561c;
  --orange-text:#f0652a;
  --white:#ffffff;
  --canvas:#e4e2e1;
  --tile-a:#e8743a;
  --tile-b:#c9551f;
  --roof-a:#c9cdd6;
  --roof-b:#8e96a6;
  --flat-a:#3d434d;
  --flat-b:#20252c;
}
*{box-sizing:border-box;margin:0;padding:0}
html,body{width:723px;height:1200px;overflow:hidden;background:var(--canvas)}
body{font-family:"Montserrat",Arial,sans-serif;color:var(--white);position:relative}

.page-slot{position:absolute;left:150px;width:423px;height:582px;box-shadow:0 6px 16px rgba(0,0,0,.35)}
.page-slot.front{top:12px}
.page-slot.back{top:606px}

.page{position:absolute;top:0;left:0;width:606px;height:835px;background:var(--ink);overflow:hidden;transform:scale(.697);transform-origin:0 0}
.page-art{position:absolute;inset:0;width:606px;height:835px}

.brand{position:absolute;left:30px;top:20px;width:200px;text-align:center;font-weight:800;color:var(--white);line-height:1}
.brand-top{font-size:40px;letter-spacing:1px}
.brand-bottom{font-size:29px;letter-spacing:.5px;margin-top:4px}

.headline{position:absolute;left:34px;top:146px;font-size:44px;font-weight:900;line-height:1;text-shadow:0 3px 4px rgba(0,0,0,.55);letter-spacing:.3px}

.thumbs{position:absolute;display:flex}
.thumb{border:3px solid var(--ink-soft);border-radius:12px;box-shadow:0 3px 6px rgba(0,0,0,.45)}

.section-title{color:var(--orange-text);font-weight:600;font-size:15px;line-height:1.15;position:absolute}
.ticks{list-style:none;font-size:11.5px;font-weight:500;line-height:18.5px;position:absolute}
.ticks.bold{font-weight:700;font-size:12px}
.ticks li{position:relative;padding-left:21px}
.ticks li.more{list-style:none}
.ticks li.tick::before{content:"";position:absolute;left:6px;top:5px;width:9px;height:9px;border-radius:50%;background:var(--orange)}
.ticks li.tick::after{content:"";position:absolute;left:9px;top:6.5px;width:2px;height:4px;border:solid var(--white);border-width:0 1.5px 1.5px 0;transform:rotate(45deg)}

.service{position:absolute;left:330px;width:270px;text-align:center;line-height:1.05}
.service-label{color:var(--orange-text);font-weight:600;font-size:15px}
.service-text{font-size:16px;font-weight:500}
.contact{position:absolute;left:330px;width:270px;text-align:center;line-height:1.05;font-weight:600}
.contact-phone{font-size:25px;font-weight:700}
.contact-web{font-size:15.5px;font-weight:500}
.contact-lic{font-size:15px}

.about{position:absolute;left:35px;top:352px;width:550px;font-size:11px;line-height:14.5px;font-weight:500}
.about p+p{margin-top:14px}
</style>
</head>
<body>

<!-- FRONT -->
<div class="page-slot front">
  <section class="page page-front">
    <svg class="page-art" viewBox="0 0 606 835" aria-hidden="false">
      <defs>
        <linearGradient id="tileGrad" x1="0" y1="0" x2="1" y2="1">
          <stop offset="0" stop-color="var(--tile-a)"/><stop offset="1" stop-color="var(--tile-b)"/>
        </linearGradient>
        <linearGradient id="roofGrad" x1="0" y1="0" x2="1" y2="1">
          <stop offset="0" stop-color="var(--roof-a)"/><stop offset="1" stop-color="var(--roof-b)"/>
        </linearGradient>
      </defs>
      <polygon points="0,100 0,337 606,428 606,0 305,0 232,100" fill="url(#tileGrad)" role="img" aria-label="Photo of orange clay tile roof"/>
      <polygon points="0,337 606,428 606,424 0,333" fill="var(--orange)"/>
      <polygon points="232,100 305,0 309,0 236,100" fill="var(--orange)"/>
      <polygon points="0,688 318,688 238,835 0,835" fill="url(#roofGrad)" role="img" aria-label="Aerial photo of grey standing-seam metal roof"/>
      <polygon points="318,688 322,688 242,835 238,835" fill="var(--orange)"/>
      <polygon points="282,755 606,755 606,835 238,835" fill="var(--orange)"/>
    </svg>

    <div class="brand"><div class="brand-top">R&amp;K</div><div class="brand-bottom">ROOFING</div></div>
    <h1 class="headline">OUR SPECIALTY IS<br>COMMERCIAL ROOFS</h1>

    <div class="thumbs" style="left:37px;top:285px;gap:8px">
      <div class="thumb" style="width:146px;height:100px;background:linear-gradient(180deg,#6f9fd8 0 35%,#d9d6cf 35%)" role="img" aria-label="Photo of white flat commercial roof under blue sky"></div>
      <div class="thumb" style="width:146px;height:100px;background:linear-gradient(180deg,#4d8fd6 0 30%,#c9d3dc 30% 62%,#6f9a8a 62%)" role="img" aria-label="Photo of commercial building with green metal roof edge"></div>
      <div class="thumb" style="width:146px;height:100px;background:linear-gradient(135deg,#f2f3f3,#c8ccd0)" role="img" aria-label="Photo of white coated flat roof"></div>
    </div>

    <h2 class="section-title" style="left:35px;top:404px">CERTIFIED WITH THE FOLLOWING MANUFACTURERS :</h2>
    <ul class="ticks bold" style="left:42px;top:428px"><li class="tick">ALTAMAX</li><li class="tick">SUMMIT</li><li class="tick">KB</li></ul>
    <ul class="ticks bold" style="left:174px;top:428px"><li class="tick">DURA-SEAL</li><li class="tick">CORVA</li></ul>
    <ul class="ticks bold" style="left:338px;top:428px"><li class="tick">PRO-SHIELD</li><li class="more">AND MORE</li></ul>

    <h2 class="section-title" style="left:35px;top:498px">R&amp;K ROOFING INSTALLS THE<br>FOLLOWING PRODUCTS:</h2>
    <ul class="ticks" style="left:36px;top:543px"><li class="tick">TPO</li><li class="tick">PVC</li><li class="tick">MODIFIED BITUMEN</li><li class="tick">SILICONE COATINGS</li><li class="tick">ACRYLIC COATINGS</li><li class="tick">SHINGLE</li></ul>
    <ul class="ticks" style="left:189px;top:543px"><li class="tick">METAL</li><li class="tick">TILE</li><li class="tick">SPRAY</li><li class="tick">POLYURETHANE</li><li class="tick">FOAM</li><li class="more">AND MORE</li></ul>

    <h2 class="section-title" style="left:339px;top:498px">R&amp;K ROOFING OFFERS THE<br>FOLLOWING SERVICES:</h2>
    <ul class="ticks" style="left:339px;top:543px"><li class="tick">NEW ROOF INSTALLATION</li><li class="tick">RE-ROOFING</li><li class="tick">ROOF MAINTENANCE AND SERVICE</li><li class="tick">ROOF INSPECTIONS</li><li class="tick">ROOF COATINGS</li><li class="more">AND MORE</li></ul>

    <div class="service" style="top:698px"><div class="service-label">SERVICE AREA:</div><div class="service-text">We service the entire<br>state of Arizona.</div></div>
    <div class="contact" style="top:768px"><div class="contact-phone">555-014-2290</div><div class="contact-web">www.rk-roofing-co.com</div><div class="contact-lic">AZ ROC 512087</div></div>
  </section>
</div>

<!-- BACK -->
<div class="page-slot back">
  <section class="page page-back">
    <svg class="page-art" viewBox="0 0 606 835">
      <defs>
        <linearGradient id="roofGrad2" x1="0" y1="0" x2="1" y2="1">
          <stop offset="0" stop-color="var(--roof-a)"/><stop offset="1" stop-color="var(--roof-b)"/>
        </linearGradient>
        <linearGradient id="flatGrad" x1="0" y1="0" x2="1" y2="1">
          <stop offset="0" stop-color="var(--flat-a)"/><stop offset="1" stop-color="var(--flat-b)"/>
        </linearGradient>
      </defs>
      <polygon points="0,100 0,338 465,338 606,428 606,0 305,0 232,100" fill="url(#roofGrad2)" role="img" aria-label="Aerial photo of grey metal roof with skylights"/>
      <polygon points="0,338 465,338 606,428 606,433 463,343 0,343" fill="var(--orange)"/>
      <polygon points="0,100 232,100 236,100 0,104" fill="var(--orange)"/>
      <polygon points="232,100 305,0 309,0 236,100" fill="var(--orange)"/>
      <polygon points="0,685 318,685 236,835 0,835" fill="url(#flatGrad)" role="img" aria-label="Photo of dark flat commercial roof with skylights"/>
      <polygon points="0,682 318,682 316,686 0,686" fill="var(--orange)"/>
      <polygon points="282,752 606,752 606,835 236,835" fill="var(--orange)"/>
    </svg>

    <div class="brand"><div class="brand-top">R&amp;K</div><div class="brand-bottom">ROOFING</div></div>

    <div class="about">
      <p>R&amp;K Roofing opened the doors in 1984, and we've since installed, serviced, maintained, and coated thousands of commercial roofs around the state of Arizona, in the many climate regions of the state.</p>
      <p>Though we all live here for the constant sunshine, Arizona is one of the harshest environments in the US for roofs. Constant sun, heat, dryness, and then the torrential monsoon downpours all test the limits of your roof.</p>
      <p>We work with you to come up with a solution that works for your roof and will keep your business dry for years to come. Then, our team of project managers, superintendents, foremen, and field workers all come together to execute on that plan and install a quality roof.</p>
      <p>We are certified with many different manufacturers, so we're able to offer custom solutions to solve your issues, that will also often come with reputable manufacturer warranties.</p>
    </div>

    <div class="thumbs" style="left:38px;top:572px;gap:48px">
      <div class="thumb" style="width:145px;height:100px;background:linear-gradient(180deg,#7fa6d6 0 25%,#8a5a44 25%)" role="img" aria-label="Photo of pitched metal roof on a building"></div>
      <div class="thumb" style="width:145px;height:100px;background:linear-gradient(135deg,#ececea,#9c9d9c)" role="img" aria-label="Photo of white roof coating being applied"></div>
      <div class="thumb" style="width:145px;height:100px;background:linear-gradient(135deg,#4a5058,#2a2f36)" role="img" aria-label="Photo of dark flat roof with skylights"></div>
    </div>

    <div class="service" style="top:695px"><div class="service-label">SERVICE AREA:</div><div class="service-text">We service the entire<br>state of Arizona.</div></div>
    <div class="contact" style="top:765px"><div class="contact-phone">555-014-2290</div><div class="contact-web">www.rk-roofing-co.com</div><div class="contact-lic">AZ ROC 512087</div></div>
  </section>
</div>

</body>
</html>
```